Rapidly Expanding Real Estate Firm Seeking Signage Designs for Multiple Properties

We would like a sign design template created that we can use at our apartment buildings. We would like a consistent sign appearance that is adaptable enough to be used at different locations, on different mediums, and in different sizes. All vary for signage depending on the local laws and regulations as well as the type and style of the property. But the sign design should be consistent enough to support our company's branding efforts; so people that see our sign know its our company but also that the specific property is unique. Our thought was to incorporate the property address; i.e. "418 Larkwood" along with a portion of our company logo(attached). Then tag our website address across the bottom. Or some combination of that structure/design. It may make sense to just use the address and website address across the bottom OR it might be good to say 418 Larkwood St in large font with "by Amber Ridge Holdings Group" underneath as sort of a tag line. Not quite sure.
But we definitely want the signage to be clearly visible, professional, and clean. Easily read for the street. Should be flexible enough to work on metal or wood or any other medium with updates for the address and maybe color.
This is not a for sale sign design request. The sign concept will be used at apartment buildings. Sample property photos are attached - we are looking for a design template that is flexible enough to work on various property types. Also could be wall mounted or a pylon sign. Concept should work either way.

Target Market(s)

Prospective Tenants 25-45 yrs of age with incomes ranging from $55k - $95k.

Industry/Entity Type

Real Estate - Apartments

Colors
59FF00
82FF00
B8FF75
E3FFCB
F4FFEA

Requirements
Must have
• The street address number, web address(www.amberridgeholdingsgroup.example), & incorporate our primary colors(green,white,black)
Nice to have
• "418 Larkwood St." by Amber Ridge
Should not have
• Should not say For Sale, For Lease, post our phone number.

```html
<!DOCTYPE html>
<html lang="en">
<head>
<meta charset="utf-8">
<title>418 Larkwood St. — Amber Ridge Holdings Group Property Sign</title>
<link rel="stylesheet" href="https://fonts.googleapis.com/css2?family=Poppins:wght@600;700&display=swap">
<style>
  :root {
    --brand-green: #7cc242;
    --brand-grey: #9c9c9c;
    --band-grey: #a9a9a9;
    --veil-grey: rgba(170, 170, 170, 0.55);
    --sign-white: #ffffff;
    --photo-sky: #eef2f5;
    --photo-glass: #8fa3b3;
  }
  html, body {
    margin: 0;
    padding: 0;
    width: 1200px;
    height: 1200px;
    overflow: hidden;
    background: var(--sign-white);
    font-family: "Poppins", sans-serif;
  }
  .property-sign {
    position: relative;
    width: 1200px;
    height: 1200px;
    background: var(--sign-white);
  }
  .sign-graphics {
    position: absolute;
    inset: 0;
  }
  .brand-name {
    position: absolute;
    right: 80px;
    top: 150px;
    margin: 0;
    font-weight: 700;
    font-size: 40px;
    letter-spacing: 1px;
    color: var(--brand-green);
    text-align: right;
    line-height: 1;
    display: flex;
    align-items: center;
    gap: 16px;
  }
  .brand-name .brand-dot {
    width: 22px;
    height: 22px;
    background: var(--brand-green);
  }
  .property-address {
    position: absolute;
    right: 80px;
    top: 260px;
    margin: 0;
    text-align: right;
    font-weight: 700;
    line-height: 0.98;
  }
  .address-number {
    display: block;
    font-size: 150px;
    color: var(--brand-green);
  }
  .address-street {
    display: block;
    font-size: 112px;
    color: var(--brand-grey);
    letter-spacing: -1px;
  }
  .owner-tagline {
    position: absolute;
    right: 96px;
    top: 630px;
    margin: 0;
    text-align: right;
    font-weight: 700;
    font-size: 52px;
    line-height: 1.02;
  }
  .owner-tagline .tag-by,
  .owner-tagline .tag-brand { color: var(--brand-green); display: block; }
  .owner-tagline .tag-group { color: var(--brand-grey); display: block; }
  .web-address {
    position: absolute;
    left: 64px;
    top: 950px;
    height: 106px;
    margin: 0;
    display: flex;
    align-items: center;
    font-weight: 600;
    font-size: 46px;
    color: var(--sign-white);
    letter-spacing: 0.2px;
  }
</style>
</head>
<body>
  <main class="property-sign">
    <svg class="sign-graphics" width="1200" height="1200" viewBox="0 0 1200 1200" aria-hidden="false">
      <defs>
        <linearGradient id="photoTone" x1="0" y1="0" x2="0" y2="1">
          <stop offset="0" stop-color="var(--sign-white)"/>
          <stop offset="0.35" stop-color="var(--photo-sky)"/>
          <stop offset="1" stop-color="var(--photo-glass)"/>
        </linearGradient>
      </defs>

      <polygon class="building-photo" role="img" aria-label="Photo of a modern glass apartment tower seen from below"
               points="48,455 48,1168 736,1168 48,455" fill="url(#photoTone)"/>

      <polygon class="accent-band-top" points="16,0 176,0 512,326 352,326" fill="var(--brand-green)"/>
      <polygon class="accent-veil-top" points="128,0 288,0 448,176 288,176" fill="var(--veil-grey)"/>

      <polygon class="accent-stripe" points="0,278 0,390 784,1200 944,1200" fill="var(--brand-green)"/>

      <polygon class="web-band" points="0,950 1136,950 1040,1056 0,1056" fill="var(--band-grey)"/>

      <polygon class="corner-wedge" points="1040,1200 1200,1046 1200,1200" fill="var(--band-grey)"/>
    </svg>

    <p class="brand-name"><span class="brand-dot"></span>AMBER RIDGE</p>

    <h1 class="property-address">
      <span class="address-number">418</span>
      <span class="address-street">LARKWOOD ST.</span>
    </h1>

    <p class="owner-tagline">
      <span class="tag-by">BY</span>
      <span class="tag-brand">AMBER RIDGE</span>
      <span class="tag-group">HOLDINGS GROUP</span>
    </p>

    <p class="web-address">www.amberridgeholdingsgroup.example</p>
  </main>
</body>
</html>
```